Brookvale Strategy Partners Website Design

I need a website design for my new business consulting and executive coaching firm, Brookvale Strategy Partners. We provide consultative services to business C-suites as well as personal coaching to executives. I have attached the logo with color scheme I have chosen. I would like the website to reflect professionalism and continue the color scheme in the logo.

Target Market(s)

Small to medium business and their executives; middle to upper income men and women in mid- to late career looking for significance

Industry/Entity Type

Business Consultant

Number of Pages Required

4 page

Requirements
Must have
• A homepage with prominent logo and way to contact for more information; an area on the homepage with easy to read, clear text to describe what the company does; a prominent area on the homepage for a tagline; a blog page that can be updated regularly, an "about us" page with biographical information; an "about us" page; a page detailing services offered
• The web design must match the logo colors and font that I have uploaded.
Nice to have
• A lighthouse picture in the background or header
Should not have
• A lot of text area on the homepage

```html
<!DOCTYPE html>
<html lang="en">
<head>
<meta charset="utf-8">
<title>Brookvale Strategy Partners</title>
<link href="https://fonts.googleapis.com/css2?family=Raleway:wght@400;500;600;700&family=Roboto:wght@400;500&display=swap" rel="stylesheet">
<style>
:root{
  --ink:#1d1d1d;
  --muted:#555;
  --blue:#1a7fd0;
  --link:#3aa6e8;
  --navy:#1c2a4f;
  --navy-deep:#162245;
  --card:#ececec;
  --dark:#262626;
  --red:#6b0f0f;
  --white:#fff;
}
*{margin:0;padding:0;box-sizing:border-box}
html,body{width:1200px;height:1200px;overflow:hidden}
body{position:relative;font-family:"Raleway",sans-serif;color:var(--ink);background:var(--white)}
.abs{position:absolute}
/* news section */
.news{position:absolute;left:0;top:0;width:1200px;height:315px;background:radial-gradient(ellipse at 20% 60%,#e4e4e4,#f6f6f6 60%,#fafafa)}
.card{position:absolute;top:-10px;width:248px;height:228px;background:var(--card);border:1px solid #d4d4d4;box-shadow:0 4px 6px rgba(0,0,0,.25);overflow:hidden}
.card .date{position:absolute;left:12px;font-size:9.5px;color:var(--blue)}
.card .title{position:absolute;left:12px;width:226px;font-size:11px;line-height:15px;color:var(--ink)}
.card .post{position:absolute;left:12px;font-size:9.5px;font-weight:600;color:var(--link)}
.feed{position:absolute;left:488px;top:0;width:228px;height:220px;overflow:hidden}
.tweet{position:absolute;left:23px;width:200px;font-size:9px;line-height:14px;color:#444}
.tweet a{color:var(--link);text-decoration:none;font-size:10.5px}
.tweet-icon{position:absolute;left:0;width:14px;height:12px}
.stamp{position:absolute;left:0;width:228px;font-size:9px;color:var(--blue);display:flex;align-items:center;gap:6px}
.stamp::before{content:"";width:12px;height:1px;background:#bbb}
.stamp::after{content:"";flex:1;height:1px;background:#ccc}
.btn-outline{position:absolute;top:233px;width:98px;height:35px;border:2px solid var(--navy);background:var(--white);font-size:11px;font-weight:700;color:var(--navy);display:flex;align-items:center;justify-content:center;letter-spacing:.3px}
/* testimonial */
.testimonial{position:absolute;left:0;top:315px;width:1200px;height:293px;background:linear-gradient(90deg,#5a5a5a 0%,#3e3e3e 45%,#2e2e2e 70%,#4a4a4a 100%)}
.testimonial-fade{position:absolute;left:0;bottom:0;width:1200px;height:50px;background:linear-gradient(to bottom,rgba(28,42,79,0),rgba(28,42,79,.7))}
.section-title{position:absolute;left:0;width:1200px;text-align:center;color:var(--white);font-weight:700}
.quote{position:absolute;left:340px;top:452px;width:530px;font-size:12.2px;line-height:22px;color:#f2f2f2;text-align:center}
.quote .mark{color:var(--link);font-size:14px;vertical-align:top}
/* stay in touch */
.touch{position:absolute;left:0;top:608px;width:1200px;height:104px;background:var(--navy-deep)}
.social{position:absolute;top:638px;width:46px;height:46px;border-radius:10px;background:var(--blue);color:var(--white);font-size:10px;font-weight:700;display:flex;align-items:center;justify-content:center}
/* contact */
.contact{position:absolute;left:0;top:712px;width:1200px;height:428px;background:var(--dark)}
.field{position:absolute;background:var(--white);font-family:"Roboto",sans-serif;font-size:10.5px;color:#333;padding:12px 14px}
.captcha{position:absolute;top:998px;height:36px;border:1px solid #cfcfcf;display:flex;align-items:center;justify-content:center;font-family:"Roboto",sans-serif;font-size:10.5px;color:var(--white)}
.submit{position:absolute;left:313px;top:1068px;width:574px;height:34px;background:var(--red);color:var(--white);font-size:12px;font-weight:700;display:flex;align-items:center;justify-content:center}
/* footer */
.footer{position:absolute;left:0;top:1140px;width:1200px;height:60px;background:var(--navy);color:var(--white);font-family:"Roboto",sans-serif;font-size:10.5px;text-align:center;padding-top:16px;line-height:15px}
.footer b{font-weight:500}
</style>
</head>
<body>

<section class="news" role="img" aria-label="Soft blurred photo of business documents on a desk"></section>

<article class="card" style="left:214px">
  <span class="date" style="top:6px">January 10, 2015</span>
  <p class="title" style="top:24px">Announce Fourth Quarter and Fiscal Year 2014 Financial Results on February 11, 2015.</p>
  <span class="date" style="top:70px">January 3, 2015</span>
  <p class="title" style="top:84px">Global Study Finds 100 Percent of Retail, 91 Percent of Entertainment and Media Organizations Breached in Trial</p>
  <span class="date" style="top:144px">December 20, 2014</span>
  <p class="title" style="top:158px">Threat Analytics Platform Integrated with LogVault to Increase Security Visibility Across the Enterprise</p>
</article>

<div class="feed">
  <svg class="tweet-icon" style="top:-2px" viewBox="0 0 14 12"><path d="M7 1C3.7 1 1 3 1 5.4c0 1.4.9 2.6 2.3 3.4L2.6 11l2.8-1.6c.5.1 1 .2 1.6.2 3.3 0 6-2 6-4.4S10.3 1 7 1z" fill="none" stroke="#1a7fd0" stroke-width="1.4"/></svg>
  <p class="tweet" style="top:-6px"><a>@Echopane</a> Pane Pro now comes with a lockscreen widget for Mobile OS 4.2</p>
  <div class="stamp" style="top:28px">6 days ago</div>

  <svg class="tweet-icon" style="top:65px" viewBox="0 0 14 12"><path d="M7 1C3.7 1 1 3 1 5.4c0 1.4.9 2.6 2.3 3.4L2.6 11l2.8-1.6c.5.1 1 .2 1.6.2 3.3 0 6-2 6-4.4S10.3 1 7 1z" fill="none" stroke="#1a7fd0" stroke-width="1.4"/></svg>
  <p class="tweet" style="top:63px">15+ Comprehensive Responsive Web Design Tutorials <a>http://lnk.ex/R7Jqa</a> /via <a>@northlinedesign</a></p>
  <div class="stamp" style="top:112px">12h Ago</div>

  <svg class="tweet-icon" style="top:150px" viewBox="0 0 14 12"><path d="M7 1C3.7 1 1 3 1 5.4c0 1.4.9 2.6 2.3 3.4L2.6 11l2.8-1.6c.5.1 1 .2 1.6.2 3.3 0 6-2 6-4.4S10.3 1 7 1z" fill="none" stroke="#1a7fd0" stroke-width="1.4"/></svg>
  <p class="tweet" style="top:147px">Most inspiring meeting ever! RT <a>@Dana Whitfield</a> Amazing meeting with the fantastic people</p>
  <div class="stamp" style="top:198px">12h ago</div>
</div>

<article class="card" style="left:738px">
  <p class="title" style="top:4px">Announce Fourth Quarter and Fiscal Year 2014 Financial Results on February 11, 2015.</p>
  <span class="post" style="top:34px">Post: Dana Whitfield, January 10, 2015</span>
  <p class="title" style="top:58px">Global Study Finds 100 Percent of Retail, 91 Percent of Entertainment and Media Organizations Breached in Trial</p>
  <span class="post" style="top:99px">Post: Dana Whitfield, January 10, 2015</span>
  <p class="title" style="top:123px;line-height:12.7px">Things are going better than I could've imagined. I started almost 4.5 months ago and have made 7% return. These market changes have provided a lot of learning lessons. Looking forward to trying some new strategies.</p>
  <span class="post" style="top:202px">Post: Dana Whitfield, January 10, 2015</span>
</article>

<a class="btn-outline" style="left:289px">VIEW MORE</a>
<a class="btn-outline" style="left:548px">FOLLOW US</a>
<a class="btn-outline" style="left:813px">VIEW MORE</a>

<section class="testimonial" role="img" aria-label="Dim photo of a consultant working at a laptop"><div class="testimonial-fade"></div></section>
<h2 class="section-title" style="top:373px;font-size:17.5px">What Our Client Say</h2>
<div class="abs" style="left:519px;top:399px;width:26px;height:2px;background:#fff"></div>
<p class="quote"><span class="mark">&ldquo;</span>Lorem ipsum dolor sit amet, consectetur adipisicing elit, sed do eiusmod tempor incididunt ut labore et dolore magna aliqua. Ut enim ad minim veniam, quis nostrud exercitation ullamco<span class="mark">&rdquo;</span></p>
<p class="section-title" style="top:518px;font-size:12.5px">Dana Whitfield</p>

<section class="touch"></section>
<h2 class="abs" style="left:357px;top:646px;font-size:22px;font-weight:700;color:#fff">YOU SHOULD STAY IN TOUCH!</h2>
<a class="social" style="left:686px">News</a>
<a class="social" style="left:741px">Video</a>
<a class="social" style="left:796px">Link</a>

<section class="contact" role="img" aria-label="Dark street map of the office neighbourhood"></section>
<h2 class="section-title" style="top:744px;font-size:21px">CONTACT US</h2>
<div class="field" style="left:248px;top:798px;width:343px;height:33px">NAME</div>
<div class="field" style="left:607px;top:798px;width:345px;height:33px">EMAIL</div>
<div class="field" style="left:248px;top:864px;width:704px;height:102px">MESSAGE</div>
<div class="captcha" style="left:466px;width:126px"><div role="img" aria-label="Captcha challenge image" style="width:80px;height:22px;background:linear-gradient(90deg,#ddd,#999)"></div></div>
<div class="captcha" style="left:607px;width:127px">Enter captcha!</div>
<a class="submit">SUBMIT YOUR MESSAGE</a>

<footer class="footer">
  &copy; 2015, <b>Brookvale Strategy Partners</b>, All Rights Reserved.<br>
  Privacy Policy &nbsp;&nbsp;| &nbsp;&nbsp;Accessibility &nbsp;&nbsp;| &nbsp;&nbsp;Contact
</footer>

</body>
</html>
```